Webpage

I am a professional genealogist. I need a webpage that is professional looking (using the logo I chose), I can add hyperlinks and photos to if and when I want.

```html
<!DOCTYPE html>
<html lang="en">
<head>
<meta charset="utf-8">
<title>Rootline Research Services</title>
<link href="https://fonts.googleapis.com/css2?family=Oxygen:wght@300;400;700&family=Open+Sans:wght@400;600&display=swap" rel="stylesheet">
<style>
:root{
  --green:#5aa882;
  --green-dark:#4c9672;
  --teal:#1fb4c6;
  --teal-dark:#0f95a8;
  --teal-active:#0c8799;
  --text:#4a4a4a;
  --muted:#6b6b6b;
  --line:#d9dcdc;
  --panel:#f1f2f2;
  --footer:#f3f5f4;
  --white:#ffffff;
}
*{box-sizing:border-box;margin:0;padding:0}
html,body{width:1200px;height:2257px;overflow:hidden;background:var(--white)}
body{font-family:"Open Sans",sans-serif;color:var(--text);position:relative}
.abs{position:absolute}
h2{font-family:"Oxygen",sans-serif;font-weight:300;color:var(--green);font-size:29px}

/* header */
.brand{left:86px;top:48px;display:flex;align-items:center;gap:16px}
.brand-dot{width:60px;height:60px;border-radius:50%;background:#a9d8c3}
.brand-name{font-family:"Oxygen",sans-serif;font-size:24px;font-weight:400;color:#3f5b55}
.call{right:86px;top:50px;text-align:right;font-family:"Oxygen",sans-serif}
.call-label{font-size:20px;color:#8a8a8a;font-weight:300}
.call-number{font-size:26px;color:var(--green)}
.call-icon{right:48px;top:64px}

/* nav */
.nav{left:0;top:155px;width:1200px;height:58px;background:linear-gradient(#29c0d1,var(--teal-dark));display:flex;padding-left:88px}
.nav a{display:flex;align-items:center;justify-content:center;height:58px;padding:0 34px;color:var(--white);font-family:"Oxygen",sans-serif;font-weight:700;font-size:16px;text-decoration:none;border-right:1px solid rgba(255,255,255,.18)}
.nav a.active{background:var(--teal-active)}

/* hero */
.hero{left:0;top:213px;width:1200px;height:509px;background:linear-gradient(100deg,#d6eef2 0%,#a9d6df 45%,#c9e7ed 100%)}
.hero-caption{left:700px;top:352px;width:366px;height:185px;background:rgba(255,255,255,.72);padding:24px 32px}
.hero-caption h3{font-family:"Oxygen",sans-serif;font-weight:400;font-size:32px;color:#2d3b3e;margin-bottom:14px}
.hero-caption p{font-size:12.5px;line-height:22px;color:#555}
.dots{left:1030px;top:678px;display:flex;gap:6px}
.dots span{width:16px;height:16px;border-radius:50%;background:#5e8e98}

/* services */
.services-title{left:86px;top:764px}
.tabs{left:108px;top:827px;display:flex;gap:8px}
.tab{height:56px;padding:0 15px;border:1px solid var(--line);border-bottom:none;display:flex;align-items:center;font-size:15px;color:#555;background:var(--white);white-space:nowrap}
.tab.active{border-top:3px solid var(--green)}
.panel{left:86px;top:883px;width:1028px;height:309px;border:1px solid var(--line);border-radius:3px}
.panel-photo{left:20px;top:34px;width:336px;height:246px;background:linear-gradient(135deg,#b5d7de,#6a98a4)}
.panel-body{left:398px;top:38px;width:610px}
.panel-body h3{font-family:"Oxygen",sans-serif;font-weight:300;font-size:31px;color:var(--green);margin-bottom:14px}
.panel-body p{font-size:13.5px;line-height:26px;color:#666;height:130px;overflow:hidden}
.btn{display:inline-flex;align-items:center;justify-content:center;background:var(--green);color:var(--white);font-family:"Oxygen",sans-serif;font-size:18px;border-bottom:3px solid var(--green-dark);border-radius:2px}
.read-more{width:144px;height:42px;margin-top:16px}

/* welcome & news */
.welcome-title{left:86px;top:1252px}
.welcome-photo{left:86px;top:1311px;width:250px;height:166px;background:linear-gradient(135deg,#9fb6bd,#3e5157)}
.welcome-text{left:366px;top:1306px;width:304px;font-size:13.5px;line-height:25px;color:#666}
.news-title{left:86px;top:1514px}
.news{left:86px;top:1566px;width:584px;list-style:none}
.news li{position:relative;padding-left:30px;font-size:14px;line-height:23px;color:#555;margin-bottom:12px}
.news li::before{content:"";position:absolute;left:2px;top:6px;width:12px;height:12px;border-radius:50%;border:2px solid #888;background:radial-gradient(#888 35%,transparent 40%)}
.more{left:626px;top:1710px;font-size:14px;color:#333;font-weight:600}

/* appointment */
.booking{left:778px;top:1260px;width:336px;height:470px;background:var(--panel);border-radius:3px;padding:24px 17px}
.booking h2{text-align:center;font-size:25px;font-weight:400;margin-bottom:20px}
.field{width:302px;height:43px;background:var(--white);border:1px solid #cfd3d3;margin-bottom:17px;padding:12px 14px;font-size:14px;color:#666}
.field.message{height:115px}
.submit{width:238px;height:50px;margin:6px 0 0 32px;font-size:20px}

/* footer */
.footer{left:0;top:1804px;width:1200px;height:453px;background:var(--footer)}
.footer-title{font-size:22px;font-weight:400;top:1860px}
.map-title{left:86px}
.map{left:86px;top:1913px;width:271px;height:192px;background:linear-gradient(135deg,#eeeadf,#dcdccd)}
.news-sub-title{left:443px}
.news-sub-text{left:443px;top:1906px;width:295px;font-size:13px;line-height:24px;color:#555}
.email-field{left:443px;top:2003px;width:293px;height:40px;background:var(--white);border:1px solid #cfd3d3;padding:10px 14px;font-size:13.5px;color:#666}
.sub-btn{left:644px;top:2067px;width:93px;height:38px;font-size:17px}
.contact-title{left:834px}
.contact-row{left:834px;display:flex;gap:18px;font-size:13px;line-height:28px;color:#555;width:280px}
.contact-row svg{flex:none;margin-top:4px}
.rule{left:86px;top:2160px;width:1028px;height:1px;background:#cfd3d3}
.copy{left:86px;top:2196px;font-size:13px;color:#333}
.social{left:972px;top:2192px;display:flex;gap:10px}
.social span{width:28px;height:28px;border-radius:50%;background:#8a8a8a}
</style>
</head>
<body>

<header>
  <div class="abs brand"><span class="brand-dot"></span><span class="brand-name">Rootline Research Services</span></div>
  <div class="abs call"><div class="call-label">Call Dana today</div><div class="call-number">+61 02 5550 1472</div></div>
  <svg class="abs call-icon" width="30" height="38" viewBox="0 0 24 30"><path d="M6 2c2 0 4 5 3 6s-3 1-2 4 4 8 7 9 3-1 4-2 6 1 6 3-3 5-5 5C10 27 1 14 2 6 2 4 4 2 6 2z" fill="var(--green)"/></svg>
</header>

<nav class="abs nav">
  <a class="active" href="#">HOME</a><a href="#">ABOUT US</a><a href="#">SERVICES</a><a href="#">CONTACT US</a><a href="#">PUBLICATIONS</a><a href="#">BLOG</a><a href="#">LINKS</a>
</nav>

<section class="abs hero" role="img" aria-label="Photo of a researcher in a mask and cap in a bright laboratory corridor"></section>
<div class="abs hero-caption">
  <h3>Forensic genealogy</h3>
  <p>Claritas est etiam processus dynamicus, qui sequitur mutationem consuetudium lectoru Mirum est notare quam littera gothica.</p>
</div>
<div class="abs dots"><span></span><span></span><span></span><span></span></div>

<h2 class="abs services-title">Our Services</h2>
<div class="abs tabs">
  <div class="tab active">Forensic genealogy</div>
  <div class="tab">kinship determination</div>
  <div class="tab">Research analysis &amp; consultation</div>
  <div class="tab">Texas researcher</div>
  <div class="tab">Record retrieval</div>
</div>
<section class="abs panel">
  <div class="abs panel-photo" role="img" aria-label="Photo of two scientists examining a flask in a lab"></div>
  <div class="abs panel-body">
    <h3>Forensic genealogy</h3>
    <p>Duis autem vel eum iriure dolor in hendrerit in vulputate velit esse molestie consequat, vel illum do lore eu feugiat nulla facilisis at vero eros et accumsan et iusto odio dignissim qui blandit praesentin uptatum zzril delenit augue duis dolore te feugait nulla facilisi. Nam liber tempor cum soluta nobis eleifend option congue nihil imperdiet doming id quod mazim placerat facer possim assum. Typi non habent claritatem insitam; est usus legentis in iis qui facit eorum claritatem. Investigationes</p>
    <span class="btn read-more">READ MORE</span>
  </div>
</section>

<h2 class="abs welcome-title">Welcome to Rootline Research Services</h2>
<div class="abs welcome-photo" role="img" aria-label="Photo of a stethoscope on a clipboard"></div>
<p class="abs welcome-text">Duis autem vel eum iriure dolor in hendrerit vulputate velit esse molestie consequat, vnllum dolore eu feugiat nulla facilisis at vero eros accumsan et iusto odio dignissim qui blandpraesent luptatum zzril delenit augue duisolore te feugait nulla facilisi. Nam liber tempor cum oluta nobis eleifend option congue.</p>

<h2 class="abs news-title">Latest News</h2>
<ul class="abs news">
  <li>Established in 1986 with 25 years of outstanding service, a GSA approved vendor</li>
  <li>A Service-Disabled Veteran-Owned company focused on hiring Service Disablieterans, Veterans and family members of veterans</li>
  <li>As a member of the Sustainable Workplace Alliance support green design, construction and operations</li>
</ul>
<span class="abs more">More..</span>

<aside class="abs booking">
  <h2>Book an Appointment</h2>
  <div class="field">Name</div>
  <div class="field">Phone</div>
  <div class="field">E-mail</div>
  <div class="field message">Message</div>
  <span class="btn submit">Submit Request</span>
</aside>

<footer class="abs footer"></footer>
<h2 class="abs footer-title map-title">Map</h2>
<div class="abs map" role="img" aria-label="Street map showing the office location"></div>

<h2 class="abs footer-title news-sub-title">Newsletter Subscription</h2>
<p class="abs news-sub-text">Lorem ipsum dolor sit amet, feugiat delicata lib isse id cum, no quo maiorum. intellegebat, liber ione eu sit. Mea cu case ludus integre.</p>
<div class="abs email-field">Enter your email id</div>
<span class="abs btn sub-btn">SUBMIT</span>

<h2 class="abs footer-title contact-title">Contact</h2>
<div class="abs contact-row" style="top:1904px">
  <svg width="20" height="26" viewBox="0 0 20 26"><path d="M10 0a9 9 0 0 1 9 9c0 7-9 17-9 17S1 16 1 9a9 9 0 0 1 9-9z" fill="#8a8a8a"/><circle cx="10" cy="9" r="3.5" fill="var(--footer)"/></svg>
  <div>Rootline Research Services<br>Dana Whitcombe (Professional Genealogist)<br>PO Box 4417<br>Austin, TX 78701</div>
</div>
<div class="abs contact-row" style="top:2033px">
  <svg width="20" height="24" viewBox="0 0 24 30"><path d="M6 2c2 0 4 5 3 6s-3 1-2 4 4 8 7 9 3-1 4-2 6 1 6 3-3 5-5 5C10 27 1 14 2 6 2 4 4 2 6 2z" fill="#8a8a8a"/></svg>
  <div>512 - 555 - 0187</div>
</div>
<div class="abs contact-row" style="top:2082px;gap:8px">
  <svg width="32" height="22" viewBox="0 0 32 22"><rect width="32" height="22" fill="#8a8a8a"/><path d="M1 1l15 11L31 1" stroke="var(--footer)" stroke-width="2" fill="none"/></svg>
  <div>dwhitcombe@example.net</div>
</div>

<div class="abs rule"></div>
<p class="abs copy">© Copyrights 2013. All Rights Reserved.</p>
<div class="abs social"><span></span><span></span><span></span><span></span></div>

</body>
</html>
```